Postcard Design

business name: COZY NEST HELPERS. I am a mother of 2 well adjusted, successful teenage boys. I decided to start this company caring for kids who are home sick, unable to go to daycare or school, and when their parent cant stay home with them. I was also a career woman for many years, with no friends available or family nearby to help when i was in an emergency situation for childcare. I know how stressful it can be when a child gets sick suddenly and unexpectedly. I would like to help out those parents in need, that have pressing schedules and a sick child at home that they really want to take care of, but cant due to their work pressures and priorities. I want parents to know that their child is safe and I can help them when in need, at last minute. The design should show the child is safe and well cared for and the parent is at ease, able to accomplish their obligations. I have also founded a nonprofit environmental education program in which I teach children in youth summer camps. I have taught creativity arts combined with science curriculum in kindergarten to 8th grade non-formal teaching for the past 5 years. This is a small community, and many people know me. I will be handing out these postcards to local daycares and people I know.

Industry/Entity Type

Business

```html
<!DOCTYPE html>
<html lang="en">
<head>
<meta charset="utf-8">
<title>Cozy Nest Helpers – Postcard</title>
<link rel="stylesheet" href="https://fonts.googleapis.com/css2?family=Shrikhand&family=Arimo:wght@400;700&family=Comic+Neue:wght@700&display=swap">
<style>
  :root {
    --paper: #fbf5f9;
    --pink: #e0509e;
    --pink-soft: #ea8dbd;
    --pink-pale: #f2b6d4;
    --magenta: #c8267c;
    --plum: #ad1a6c;
    --band: rgba(214, 140, 176, 0.55);
    --photo-a: #dfe9f5;
    --photo-b: #9fbde0;
    --white: #ffffff;
  }
  * { margin: 0; padding: 0; box-sizing: border-box; }
  html, body { width: 930px; height: 1200px; overflow: hidden; background: var(--paper); }
  .postcard {
    position: relative;
    width: 930px;
    height: 1200px;
    overflow: hidden;
    background: var(--paper);
    font-family: "Arimo", Arial, sans-serif;
  }
  .backdrop { position: absolute; inset: 0; width: 930px; height: 1200px; }
  .brand-title {
    position: absolute;
    top: 48px; left: 0; width: 930px;
    text-align: center;
    font-family: "Shrikhand", cursive;
    font-size: 58px;
    letter-spacing: 1px;
    color: var(--pink);
    text-shadow: 2px 2px 0 var(--white), 3px 4px 4px rgba(173, 26, 108, 0.35);
  }
  .brand-tagline {
    position: absolute;
    top: 116px; left: 0; width: 930px;
    text-align: center;
    font-size: 33px;
    color: var(--magenta);
  }
  .hero-photo {
    position: absolute;
    left: 220px; top: 183px;
    width: 490px; height: 321px;
    background: linear-gradient(135deg, var(--photo-a) 0%, #f3f5f8 45%, var(--photo-b) 100%);
    box-shadow: 0 0 14px 4px rgba(224, 80, 158, 0.3);
  }
  .intro-band {
    position: absolute;
    left: 0; top: 553px;
    width: 930px; height: 121px;
    background: var(--band);
    display: flex; align-items: center; justify-content: center;
  }
  .intro-band p {
    width: 720px;
    text-align: center;
    color: var(--white);
    font-size: 20px;
    line-height: 29px;
  }
  .mission {
    position: absolute;
    top: 702px; left: 0; width: 930px;
    text-align: center;
    color: var(--magenta);
    font-size: 24px;
    line-height: 34px;
    text-shadow: 1px 1px 1px rgba(173, 26, 108, 0.25);
  }
  .mission strong { font-size: 30px; font-weight: 700; }
  .contact {
    position: absolute;
    top: 815px; left: 0; width: 930px;
    text-align: center;
    font-family: "Shrikhand", cursive;
    color: var(--pink);
    text-shadow: 1px 2px 2px rgba(173, 26, 108, 0.3);
  }
  .contact-name { font-size: 32px; line-height: 40px; }
  .contact-phone { font-size: 34px; line-height: 40px; }
  .call-badge {
    position: absolute;
    left: 704px; top: 962px;
    width: 168px; height: 168px;
    border-radius: 50%;
    background: var(--pink);
    border: 3px solid var(--pink-pale);
    display: flex; align-items: center; justify-content: center;
    text-align: center;
    font-family: "Comic Neue", "Comic Sans MS", cursive;
    font-weight: 700;
    font-size: 23px;
    line-height: 29px;
    color: var(--white);
  }
</style>
</head>
<body>
<main class="postcard">
  <svg class="backdrop" viewBox="0 0 930 1200" aria-hidden="true">
    <polygon points="0,0 160,0 0,82" fill="var(--pink-soft)"/>
    <polygon points="0,905 930,810 930,1200 0,1200" fill="var(--pink-pale)"/>
    <polygon points="0,935 300,1000 930,840 930,1200 0,1200" fill="var(--pink-soft)"/>
    <polygon points="0,980 290,1060 0,1200" fill="var(--pink)"/>
    <polygon points="230,1065 930,865 930,1200 0,1200 0,1110" fill="var(--magenta)"/>
    <polygon points="370,1200 930,990 930,1200" fill="var(--plum)"/>
  </svg>

  <h1 class="brand-title">COZY NEST HELPERS</h1>
  <p class="brand-tagline">Professional Child Care Centre</p>

  <div class="hero-photo" role="img" aria-label="Photo of a child resting on a pale blue pillow, hugging a teddy bear"></div>

  <section class="intro-band">
    <p>Are you constantly struggling to find a trusted friend or relative to take care of your sick child when daycare or school is not an option for the day? Rest assured! Cozy Nest Helpers can help in any emergency situation.</p>
  </section>

  <p class="mission"><strong>Our mission</strong> is to provide emergency childcare<br>for your sick child when you have no alternatives.</p>

  <div class="contact">
    <p class="contact-name">Dana Whitfield</p>
    <p class="contact-phone">(555) 218-4907</p>
  </div>

  <div class="call-badge">CALL<br>TODAY TO<br>LEARN<br>MORE</div>
</main>
</body>
</html>
```